Business Card for Freelance Copywriting & Web Design Business

Hi! I have a logo but want a new business card. Here's a better idea of what I'm thinking:
-Brand new double-sided business card, rounded cards, embossed logo, nice quality paper
-Include phone (604-382-9145), email (hello@linnearowatt.org), and website (www.linnearowatt.org). No address, please, since I service clients worldwide.
-I'd like the fonts to match those on my website (www.linnearowatt.org). I had to purchase the one font (Born Ready), attached. I'm not sure which version was used on my site so I included all that I purchased. The secondary font is Helvetica
-I'd also like the tagline "Powerful Words. Impressive Results." included.
-My primary brand colour is the teal, colour #19ADC3
Linnea Rowatt | Linnea Rowatt Copywriting & Web Design <hello@linnearowatt.org>
-I'd also like the following services listed on the new cards:
SEO Website Content
SEO Blog Content
SEO Website Design
Contact Information for Business Card
as stated in brief
Font styles to use
Other font styles liked:
- See brief
Look and feel
Each slider illustrates characteristics of the customer's brand and the style your logo design should communicate.

```html
<!DOCTYPE html>
<html lang="en">
<head>
<meta charset="utf-8">
<title>Linnea Rowatt – Business Card</title>
<link href="https://fonts.googleapis.com/css2?family=Arimo:wght@400;700&family=Kristi&display=swap" rel="stylesheet">
<style>
  :root {
    --bg: #e9eaeb;
    --card: #fbfbfa;
    --teal: #19adc3;
    --teal-soft: #6fbfca;
    --ink: #111111;
    --grey: #4a4a4a;
  }
  * { box-sizing: border-box; margin: 0; padding: 0; }
  html, body { width: 1200px; height: 900px; overflow: hidden; }
  body {
    background: var(--bg);
    font-family: "Arimo", Helvetica, Arial, sans-serif;
    display: flex; flex-direction: column; align-items: center; justify-content: center; gap: 48px;
  }
  .card {
    position: relative; width: 640px; height: 366px;
    background: var(--card); border-radius: 30px;
    box-shadow: 0 14px 30px rgba(0,0,0,.18);
    overflow: hidden;
  }
  .card__decor {
    position: absolute; left: 60px; top: 120px; width: 190px; height: 260px;
    background: radial-gradient(ellipse at center, rgba(111,191,202,.28), rgba(111,191,202,0) 70%);
  }
  .brand {
    position: absolute; right: 70px; top: 62px;
    display: flex; align-items: center; gap: 10px;
  }
  .brand__dot { width: 14px; height: 14px; border-radius: 50%; background: var(--teal); }
  .brand__name { font-size: 30px; font-weight: 700; color: var(--ink); letter-spacing: .5px; }
  .rule { position: absolute; height: 1px; background: var(--teal-soft); }
  .services__title {
    position: absolute; left: 44px; top: 255px;
    color: var(--teal); font-weight: 700; font-size: 19px;
  }
  .front .rule { left: 150px; right: 40px; top: 268px; }
  .services__list {
    position: absolute; left: 44px; top: 292px;
    font-size: 18px; color: var(--ink);
  }
  .back .rule { left: 250px; right: 40px; top: 205px; }
  .person { position: absolute; left: 44px; top: 158px; }
  .person__name { font-family: "Kristi", cursive; font-size: 58px; color: var(--ink); line-height: 1; }
  .person__role { color: var(--teal); font-size: 18px; margin-top: 2px; }
  .contact { position: absolute; left: 44px; top: 262px; list-style: none; }
  .contact li {
    display: flex; align-items: center; gap: 10px;
    font-size: 17px; color: var(--grey); height: 26px;
  }
  .contact svg { width: 16px; height: 16px; stroke: var(--teal); fill: none; stroke-width: 1.6; }
  .tagline {
    position: absolute; right: 40px; bottom: 52px;
    font-size: 14px; font-weight: 700; color: var(--ink);
  }
</style>
</head>
<body>
  <section class="card front">
    <div class="card__decor" role="img" aria-label="Faint teal decorative motif"></div>
    <div class="brand"><span class="brand__dot"></span><span class="brand__name">Linnea Rowatt</span></div>
    <h2 class="services__title">Services</h2>
    <div class="rule"></div>
    <p class="services__list">SEO Website Content | SEO Blog Content | SEO Website Design</p>
  </section>

  <section class="card back">
    <div class="card__decor" role="img" aria-label="Faint teal decorative motif"></div>
    <div class="brand"><span class="brand__dot"></span><span class="brand__name">Linnea Rowatt</span></div>
    <div class="rule"></div>
    <div class="person">
      <h1 class="person__name">Linnea Rowatt</h1>
      <p class="person__role">Copywriting &amp; Web Design</p>
    </div>
    <ul class="contact">
      <li><svg viewBox="0 0 16 16"><path d="M3 2h3l1.5 3.5-2 1.2a8 8 0 0 0 3.8 3.8l1.2-2L14 10v3a1 1 0 0 1-1 1A11 11 0 0 1 2 3a1 1 0 0 1 1-1z"/></svg>604-382-9145</li>
      <li><svg viewBox="0 0 16 16"><rect x="1.5" y="3.5" width="13" height="9"/><path d="M1.5 3.5 8 9l6.5-5.5"/></svg>hello@linnearowatt.org</li>
      <li><svg viewBox="0 0 16 16"><circle cx="8" cy="8" r="6.5"/><path d="M1.5 8h13M8 1.5c-3 3.5-3 9.5 0 13M8 1.5c3 3.5 3 9.5 0 13"/></svg>www.linnearowatt.org</li>
    </ul>
    <p class="tagline">Powerful Words. Impressive Results.</p>
  </section>
</body>
</html>
```